Advertising agency needs site design

You will be designing a clean (plenty of white space) and vivid (colorful) design that is for an advertising agency named Beacon Brightly. Their current web site is located at www.BeaconBrightly.net. From there you can see their services and get a feel for the company as the site stands today.
The following are direct quotes from the client:
“I want a clean look with colors of the teal blue, deep yellow (in logo) and then a good energetic orange (deep orange - rich) should bring a good feel and enthusiasm.”
“The orange can be a nice accent color, not dominant.”
“Saw two other things I like - the website fizzlarkstudio.com was pretty cool. I liked how the top banner changed colors as you moved to different tabs. I am somewhat wanting the colors I mentioned - like the blue color we use can be lighter as long as it works with the logo. - love the zing leaves site. I want quirky, creative and clean look - fun feel but slightly sophisticated to work with the medical field.”
Beacon Brightly currently focuses on the following primary industries:
• Medical / Health Care – Currently the primary industry
• Retail Industry
• Automotive Industry
• Entertainment Industry
Primary Services
• Media Planning & Buying: Web, TV, Print, Radio
• Campaign monitoring and reporting
• Commercial Production: TV & Radio
• Strategic Planning
• Market Research
• Internet Marketing: Email, SEO, Web design / development
Primary Navigation will consist of the following:
• Home
• About Us
o History
o Principal Profile (sub nav)
o Sales Team & Partners
• Clients
• Services
• Testimonials
• Contact Us
They want the web site to act as a basis for future marketing collateral so the overall feel from the web site must be capable of translating to print and other collateral. I do not currently have a clean digital version of their logo however their logo is on the web site (beaconbrightly.net)
Target Market(s)
larger companies that are purchasing air time on television and radio. Typically in the health care industry and others described above in brief.
Industry/Entity Type
Advertising
Look and feel

```html
<!DOCTYPE html>
<html lang="en">
<head>
<meta charset="utf-8">
<title>Beacon Brightly — Advertising Agency</title>
<link href="https://fonts.googleapis.com/css2?family=Arimo:wght@400;700&family=Lora:ital,wght@0,700;1,400&display=swap" rel="stylesheet">
<style>
:root{
  --teal:#1e6f8c;
  --teal-dark:#0d3550;
  --navy:#0a2d45;
  --orange:#fbb03b;
  --orange-deep:#f09a1a;
  --ink:#555;
  --ink-dark:#333;
  --line:#e2e2e2;
  --tab-health:#1c9cb2;
  --tab-retail:#5ea624;
  --tab-auto:#dc4a10;
  --tab-ent:#6b3a98;
  --white:#fff;
}
*{margin:0;padding:0;box-sizing:border-box}
html,body{width:963px;height:1200px;overflow:hidden}
body{position:relative;background:var(--white);font-family:"Arimo",Arial,sans-serif;color:var(--ink)}
.header{position:absolute;left:0;top:0;width:963px;height:103px;background:linear-gradient(#fff,#ececec)}
.brand{position:absolute;left:62px;top:36px;font-size:34px;color:var(--teal);letter-spacing:1px}
.brand-mark{display:inline-block;width:12px;height:12px;background:var(--orange);margin-right:8px;vertical-align:middle}
.account{position:absolute;right:55px;top:12px;font-size:11px;font-weight:700;color:var(--teal);letter-spacing:.5px}
.account span{margin:0 6px;color:#999}
.call{position:absolute;left:660px;top:44px;width:215px;height:48px;background:var(--white);border-radius:4px;box-shadow:0 1px 3px rgba(0,0,0,.25)}
.call-agent{position:absolute;left:4px;top:-20px;width:54px;height:64px;border-radius:6px;background:linear-gradient(#e0a070,#c0482a)}
.call-label{position:absolute;left:72px;top:6px;font-size:13px;font-weight:700;color:var(--teal)}
.call-number{position:absolute;left:72px;top:22px;font-size:20px;color:var(--teal)}
.nav{position:absolute;left:0;top:103px;width:963px;height:32px;background:linear-gradient(#fdfdfd,#eaeaea);border-top:1px solid #ddd;border-bottom:1px solid #ddd}
.nav ul{list-style:none;position:absolute;left:44px;top:0;display:flex}
.nav li{height:30px;line-height:30px;padding:0 19px;font-size:13px;color:var(--teal);border-right:1px solid #d8d8d8}
.nav li:last-child{border-right:0}
.search{position:absolute;left:706px;top:4px;width:197px;height:23px;background:var(--white);border:1px solid #ccc;font-size:11px;color:#999;line-height:21px;padding-left:8px}
.search svg{position:absolute;right:5px;top:4px}
.band{position:absolute;left:0;top:135px;width:963px;height:260px;background:var(--orange)}
.card{position:absolute;left:44px;top:148px;width:876px;height:820px;background:var(--white);border-radius:4px 4px 0 0;box-shadow:0 0 4px rgba(0,0,0,.2)}
.slider{position:absolute;left:4px;top:2px;width:868px;height:282px;background:linear-gradient(100deg,#2c6f80 0%,#3c8c96 40%,#2a5a7a 75%,#1d3d5c 100%);border-bottom:4px solid #d9d9d9}
.slider-photo{position:absolute;right:0;top:0;width:300px;height:278px;background:linear-gradient(160deg,#4b7a92,#1f3d54)}
.slider-title{position:absolute;left:42px;top:76px;font-family:"Lora",Georgia,serif;font-weight:700;font-size:29px;color:var(--orange);letter-spacing:1px}
.slider-text{position:absolute;left:42px;top:114px;width:380px;font-family:"Lora",Georgia,serif;font-style:italic;font-size:20px;line-height:26px;color:var(--white)}
.dots{position:absolute;left:40px;top:260px;display:flex;gap:8px}
.dots i{width:13px;height:13px;border-radius:50%;background:#c8c8c8}
.dots i:first-child{background:var(--orange)}
.tabs{position:absolute;left:9px;top:300px;display:flex;gap:10px}
.tab{position:relative;width:207px;height:40px;border-radius:4px;color:var(--white);font-size:17px;line-height:40px;padding-left:12px}
.tab svg{position:absolute;right:4px;top:2px}
.tab-health{background:var(--tab-health)}.tab-retail{background:var(--tab-retail)}.tab-auto{background:var(--tab-auto)}.tab-ent{background:var(--tab-ent)}
.welcome{position:absolute;left:18px;top:358px;width:572px}
.welcome h2{font-weight:400;font-size:18px;color:var(--ink);margin-bottom:10px}
.welcome h2 b{font-weight:400;color:var(--teal)}
.welcome p{font-size:11px;line-height:19.5px;text-align:justify;color:var(--ink)}
.services{position:absolute;left:613px;top:358px;width:253px}
.services h3{font-weight:400;font-size:18px;color:var(--ink);margin-bottom:9px}
.services ul{list-style:none}
.services li{position:relative;height:24px;line-height:24px;margin-bottom:2.5px;background:#ebebeb;font-size:12px;color:var(--ink);padding-left:27px;border-left:1px solid #d5d5d5}
.services li::before{content:"";position:absolute;left:8px;top:8px;border-left:5px solid var(--teal);border-top:4px solid transparent;border-bottom:4px solid transparent}
.lower{position:absolute;left:0;top:569px;width:876px;height:251px;background:var(--orange)}
.lower h3{font-weight:400;font-size:17px;color:var(--ink-dark)}
.news{position:absolute;left:11px;top:4px;width:230px}
.news-item{padding:12px 0 6px;border-bottom:1px dashed #fff3}
.news-date{font-size:11px;font-weight:700;color:var(--white)}
.news-text{font-size:11px;line-height:15px;color:var(--white)}
.more{text-align:right;font-size:10px;font-weight:700;color:var(--ink-dark);margin-top:6px}
.testi{position:absolute;left:315px;top:4px;width:220px}
.quote{position:relative;margin-top:8px;width:220px;height:134px;background:#f4f4f4;border-radius:18px;padding:18px 16px 0 24px;font-size:11px;line-height:15px;color:var(--ink)}
.quote::before{content:"\201C";position:absolute;left:10px;top:10px;font-size:20px;color:var(--ink-dark)}
.quote svg{position:absolute;left:30px;bottom:-22px}
.arrows{text-align:right;font-size:11px;font-weight:700;color:var(--ink-dark);margin-top:2px}
.author{margin-top:6px;padding-left:18px;font-size:11px;line-height:19px;color:#7a5a20}
.author b{font-style:italic;color:var(--teal-dark)}
.newsletter{position:absolute;left:639px;top:4px;width:225px}
.newsletter p{font-size:11px;color:var(--white);margin:8px 6px}
.email{width:221px;height:27px;background:var(--white);border-radius:4px;font-size:11px;color:#999;line-height:27px;padding-left:12px}
.submit{margin:12px 0 0 138px;width:85px;height:25px;background:#333;border-radius:4px;color:var(--white);font-size:13px;font-weight:700;text-align:center;line-height:25px;letter-spacing:1px}
.clients-title{margin:-14px 0 0 10px}
.client-box{margin:10px 0 0 16px;width:194px;height:72px;background:var(--white);border-radius:6px;font-size:17px;font-weight:700;color:var(--ink-dark);text-align:center;line-height:25px;padding-top:11px;letter-spacing:1px}
.client-arrows{text-align:right;font-size:11px;font-weight:700;color:var(--teal-dark);margin-top:6px;padding-right:10px}
.footer{position:absolute;left:44px;top:965px;width:876px;height:235px;background:var(--teal-dark)}
.fcol{position:absolute;top:14px}
.fcol h4{font-size:11.5px;font-weight:700;color:var(--white);letter-spacing:1px;margin-bottom:12px}
.fcol ul{list-style:none;padding-left:12px}
.fcol li{position:relative;font-size:10.5px;line-height:21px;color:var(--white)}
.fcol li::before{content:"";position:absolute;left:-11px;top:9px;width:4px;height:4px;border-radius:50%;background:var(--white)}
.social li{width:95px}
.social li i{position:absolute;right:0;top:5px;width:11px;height:11px;background:var(--orange)}
.contact p{font-size:10.5px;line-height:19px;color:var(--white)}
.contact .tel{margin-top:8px;padding-left:35px;position:relative}
.contact .tel svg{position:absolute;left:2px;top:4px}
.copyright{position:absolute;left:0;bottom:0;width:876px;height:46px;background:var(--navy);text-align:center;line-height:34px;font-size:10.5px;color:#cfd8df;letter-spacing:1px}
</style>
</head>
<body>
<header class="header">
  <div class="brand"><i class="brand-mark"></i>beacon brightly</div>
  <div class="account">LOGIN<span>|</span>SIGN UP</div>
  <div class="call">
    <div class="call-agent" role="img" aria-label="Illustrated support agent with headset"></div>
    <div class="call-label">CALL US</div>
    <div class="call-number">555 014 2290</div>
  </div>
</header>
<nav class="nav">
  <ul><li>Home</li><li>About Us</li><li>Clients</li><li>Services</li><li>Testimonials</li><li>Contact Us</li></ul>
  <div class="search">Search
    <svg width="13" height="13" viewBox="0 0 13 13"><circle cx="5.5" cy="5.5" r="4" fill="none" stroke="#1e6f8c" stroke-width="2"/><line x1="8.5" y1="8.5" x2="12" y2="12" stroke="#1e6f8c" stroke-width="2.5"/></svg>
  </div>
</nav>
<div class="band"></div>
<main class="card">
  <section class="slider">
    <div class="slider-photo" role="img" aria-label="Photo of a businesswoman looking upward in front of office glass"></div>
    <h1 class="slider-title">LOREM IPSUM DOLOR SIT</h1>
    <p class="slider-text">Lorem ipsum dolor sit amet, consectetuer adipiscing elit. Aenean commodo l igula eget dolor.</p>
    <div class="dots"><i></i><i></i><i></i><i></i></div>
  </section>
  <div class="tabs">
    <div class="tab tab-health">Medical / Health<svg width="30" height="36" viewBox="0 0 30 36"><path d="M2 34 C14 30 12 6 28 2" fill="none" stroke="#fff" stroke-width="1.5"/><path d="M22 28h6M25 25v6" stroke="#fff" stroke-width="1.5"/></svg></div>
    <div class="tab tab-retail">Retail<svg width="30" height="36" viewBox="0 0 30 36"><path d="M2 34 C14 30 12 6 28 2" fill="none" stroke="#fff" stroke-width="1.5"/><path d="M22 28h6M25 25v6" stroke="#fff" stroke-width="1.5"/></svg></div>
    <div class="tab tab-auto">Automotive<svg width="30" height="36" viewBox="0 0 30 36"><path d="M2 34 C14 30 12 6 28 2" fill="none" stroke="#fff" stroke-width="1.5"/><path d="M22 28h6M25 25v6" stroke="#fff" stroke-width="1.5"/></svg></div>
    <div class="tab tab-ent">Entertainment<svg width="30" height="36" viewBox="0 0 30 36"><path d="M2 34 C14 30 12 6 28 2" fill="none" stroke="#fff" stroke-width="1.5"/><path d="M22 28h6M25 25v6" stroke="#fff" stroke-width="1.5"/></svg></div>
  </div>
  <section class="welcome">
    <h2>Welcome to <b>beacon brightly</b></h2>
    <p>Lorem ipsum dolor sit amet, consectetuer adipiscing elit. Aenean commodo ligula eget dolor. Aenean massa. Cum sociis natoque penatibus et magnis dis parturient montes, nascetur ridiculus mus. Donec quam felis, ultricies nec, pellentesque eu, pretium quis, sem. Nulla consequat massa quis enim. Donec pede justo, fringilla vel, aliquet nec, vulputate eget, arcu.Lorem ipsum dolor sit amet, consectetuer adipiscing elit. Aenean commodo ligula eget dolor. Aenean massa. Cum sociis natoque gnis dis parturient montes, nascetur ridiculus mus. Donec quam felis, ultricies nec, pellentesque eu, pretium quis, sem. Nulla consequat massa quis enim. Donec pede justo, fringilla vel, aliquet nec, vulputate eget, arcu.n commodo ligula eget dolor. Aenean massa.</p>
  </section>
  <aside class="services">
    <h3>Services</h3>
    <ul>
      <li>Media Planning &amp; Buying</li>
      <li>Campaign monitoring and reporting</li>
      <li>Commercial Production</li>
      <li>Strategic Planning</li>
      <li>Market Research</li>
      <li>Internet Marketing</li>
    </ul>
  </aside>
  <section class="lower">
    <div class="news">
      <h3>News</h3>
      <div class="news-item"><div class="news-date">MAY 19, 2011</div><div class="news-text">Lorem ipsum dolor sit ametconsectetuer adipiscing elit. Aenean</div></div>
      <div class="news-item"><div class="news-date">MAY 19, 2011</div><div class="news-text">Lorem ipsum dolor sit ametconsectetuer adipiscing elit. Aenean</div></div>
      <div class="news-item"><div class="news-date">MAY 19, 2011</div><div class="news-text">Lorem ipsum dolor sit ametconsectetuer adipiscing elit. Aenean</div></div>
      <div class="more">Read more &gt;&gt;</div>
    </div>
    <div class="testi">
      <h3>Testimonials</h3>
      <div class="quote">Lorem ipsum dolor sit ametcon-sectetuer adipiscing elit. Aenean commodo ligula eget doloAenean massa. Cum eget doloAenean massa. Cum sociis sociis
        <svg width="26" height="24" viewBox="0 0 26 24"><path d="M0 0h26L6 24z" fill="#f4f4f4"/></svg>
      </div>
      <div class="arrows">&lt; &gt;</div>
      <div class="author"><b>Name</b>, webdesigner<br>hello@pinewickmail.com</div>
    </div>
    <div class="newsletter">
      <h3>Newsletter</h3>
      <p>Sign up for our Newsletters</p>
      <div class="email">Enter you email</div>
      <div class="submit">SUBMIT</div>
      <h3 class="clients-title">Our Clients</h3>
      <div class="client-box">HERE COMES LOGO<br>CLIENTS</div>
      <div class="client-arrows">&lt; &gt;</div>
    </div>
  </section>
</main>
<footer class="footer">
  <div class="fcol" style="left:13px"><h4>Company</h4><ul><li>Home</li><li>About Us</li><li>Contact Us</li><li>Privacy Policy</li><li>Tearms of use</li></ul></div>
  <div class="fcol" style="left:145px"><h4>Industries</h4><ul><li>Medical / Health Care</li><li>Retail</li><li>Automotive</li><li>Entertainment</li></ul></div>
  <div class="fcol" style="left:317px"><h4>Services</h4><ul><li>Media Planning &amp; Buying C</li><li>Campaign monitoring and reporting</li><li>Commercial Production</li><li>Strategic Planning</li><li>Market Research</li><li>Internet Marketing</li></ul></div>
  <div class="fcol social" style="left:556px"><h4>Follow Us</h4><ul><li>Rss<i></i></li><li>Chatterly<i></i></li><li>Circleboard<i></i></li></ul></div>
  <div class="fcol contact" style="left:694px"><h4>Contact Us</h4>
    <p>Beacon Brightly, Inc.<br>4120 Larkmoor Avenue, Suite 310<br>Fernvale, Texas 75990</p>
    <p class="tel"><svg width="16" height="12" viewBox="0 0 16 12"><path d="M1 4c4-4 10-4 14 0l-2 2-2-1V3H5v2L3 6z M4 7h8l2 4H2z" fill="#fff"/></svg>555.018.4471 &nbsp;(P)</p>
    <p class="tel" style="margin-top:2px"><svg width="16" height="12" viewBox="0 0 16 12"><rect x="4" y="0" width="8" height="4" fill="#fff"/><rect x="1" y="4" width="14" height="5" fill="#fff"/><rect x="4" y="8" width="8" height="4" fill="#fff" stroke="#0d3550"/></svg>555.018.4472 &nbsp;(F)</p>
  </div>
  <div class="copyright">2011 © beaconbrightly.com. All rights reserved.</div>
</footer>
</body>
</html>
```